R J Penn Accounting & SMSF Auditing needs a Web Site Design

I need some examples of what a web design can look like for my business.
The business name is above and I have already registered a domain name of www.penn-smsf.com.au
I have attached my current letterhead and business cards and would like to maintain these colours basically Red on White with some black

Industry/Entity Type

Business

```html
<!DOCTYPE html>
<html lang="en">
<head>
<meta charset="utf-8">
<title>Harwick Audit &amp; Accounting</title>
<link rel="stylesheet" href="https://fonts.googleapis.com/css2?family=Oswald:wght@300;400;500;700&family=Open+Sans:wght@400;600;700&display=swap">
<style>
:root{
  --red:#c8102e;
  --black:#1b1b1b;
  --charcoal:#262626;
  --ink:#333333;
  --grey:#666666;
  --white:#ffffff;
  --heading:'Oswald', 'Arial Narrow', sans-serif;
  --body:'Open Sans', Arial, sans-serif;
}
*{margin:0;padding:0;box-sizing:border-box;}
html,body{width:1200px;height:3103px;overflow:hidden;}
body{background:var(--white);font-family:var(--body);color:var(--ink);position:relative;}
a{text-decoration:none;color:inherit;}
.container{width:960px;margin:0 auto;position:relative;height:100%;}

/* Header */
.site-header{height:96px;background:var(--white);box-shadow:0 1px 4px rgba(0,0,0,.12);position:relative;z-index:2;}
.site-header .container{display:flex;align-items:center;justify-content:space-between;width:1000px;}
.brand{font-family:var(--heading);font-weight:700;font-size:30px;color:var(--red);letter-spacing:.5px;white-space:nowrap;}
.main-nav{display:flex;height:96px;}
.main-nav a{font-family:var(--heading);font-size:13px;color:var(--black);display:flex;align-items:center;padding:0 20px;letter-spacing:.4px;white-space:nowrap;}
.main-nav a.active{background:var(--red);color:var(--white);}

/* Hero */
.hero{height:532px;position:relative;background:linear-gradient(100deg,#5a3a28 0%,#8c6646 35%,#c9a582 60%,#e9d8c3 78%,#9c7a5c 100%);}
.hero-copy{position:absolute;left:154px;top:190px;color:var(--white);}
.hero-title{font-family:var(--heading);font-weight:700;font-size:38px;letter-spacing:.5px;line-height:1.1;}
.hero-sub{font-family:var(--heading);font-weight:300;font-size:30px;line-height:1.2;opacity:.9;}
.btn-outline{display:inline-block;border:2px solid var(--white);color:var(--white);font-family:var(--heading);font-size:20px;width:206px;height:44px;line-height:40px;text-align:center;margin-right:26px;}
.hero .actions{margin-top:38px;}

.section-title{font-family:var(--heading);font-weight:400;font-size:34px;text-align:center;color:var(--black);}

/* Our firm */
.firm{height:452px;padding-top:40px;}
.firm-grid{display:flex;justify-content:space-between;width:1000px;margin:45px auto 0;}
.firm-item{width:220px;text-align:center;}
.firm-icon{width:128px;height:128px;border:2px solid var(--red);border-radius:50%;margin:0 auto;display:flex;align-items:center;justify-content:center;}
.item-title{font-family:var(--heading);font-size:15px;font-weight:500;color:var(--black);margin-top:36px;}
.item-text{font-size:12px;line-height:1.45;color:var(--grey);margin:8px auto 0;width:190px;}
.read-more{display:block;font-family:var(--heading);font-size:12px;color:var(--red);margin-top:16px;}

/* Services */
.services{height:429px;background:var(--red);padding-top:36px;}
.services .section-title{color:var(--white);font-weight:300;}
.service-grid{display:flex;justify-content:center;gap:55px;margin-top:26px;}
.service-card{width:233px;text-align:center;color:var(--white);}
.service-photo{height:110px;}
.photo-law{background:linear-gradient(135deg,#e8e1d6,#b89b72 60%,#6d5238);}
.photo-gavel{background:linear-gradient(135deg,#d3a24c,#8a5a22 55%,#3c2611);}
.photo-advisor{background:linear-gradient(135deg,#e9eef2,#b9c4cc 55%,#7d8a94);}
.service-label{background:var(--black);font-family:var(--heading);font-size:15px;height:35px;line-height:35px;}
.service-card .item-text{color:#f6d9de;width:210px;margin-top:14px;}
.service-card .read-more{color:var(--white);}

/* Banner */
.banner{height:353px;position:relative;background:linear-gradient(100deg,#1e2a3c 0%,#2f3a4a 35%,#5b4636 62%,#8a5f3d 78%,#3a2d25 100%);}
.banner-copy{position:absolute;left:137px;top:92px;color:var(--white);}
.banner-title{font-family:var(--heading);font-weight:400;font-size:36px;line-height:1.15;}
.banner .btn-outline{margin-top:20px;}

/* About */
.about{height:360px;position:relative;}
.about-photo{position:absolute;left:171px;top:32px;width:206px;height:328px;background:linear-gradient(180deg,#f2f2f2,#cfc7c0 45%,#8f9296 100%);}
.about-copy{position:absolute;left:446px;top:60px;width:634px;}
.about-title{font-family:var(--heading);font-weight:400;font-size:34px;color:var(--black);}
.about-text{font-size:12.5px;line-height:1.5;color:var(--grey);margin-top:10px;}
.btn-red{display:inline-block;background:var(--red);color:var(--white);font-family:var(--heading);font-size:17px;width:136px;height:44px;line-height:44px;text-align:center;border-radius:4px;margin-top:22px;}

/* Team */
.team{height:446px;background:var(--charcoal);padding-top:34px;}
.team-title{font-family:var(--heading);font-weight:400;font-size:34px;color:var(--white);width:1000px;margin:0 auto;}
.team-grid{display:flex;justify-content:center;gap:82px;margin-top:42px;}
.team-card{width:194px;}
.team-photo{height:223px;background:linear-gradient(180deg,#f4f4f4,#cdd3d8 55%,#7b8791 100%);}
.team-label{background:var(--red);color:var(--white);font-family:var(--heading);font-size:14px;text-align:center;height:45px;line-height:45px;}

/* Testimonial */
.testimonial{height:299px;padding-top:34px;text-align:center;}
.testimonial .section-title{font-weight:300;font-size:32px;}
.avatar{width:72px;height:72px;border-radius:50%;border:3px solid var(--red);margin:18px auto 0;background:linear-gradient(180deg,#e4d9cf,#a98f7c);}
.quote{position:relative;width:800px;margin:22px auto 0;font-size:12px;line-height:1.55;color:var(--grey);}
.quote-mark{position:absolute;top:-20px;font-family:Georgia,serif;font-size:60px;color:var(--red);line-height:1;}
.quote-mark.open{left:-40px;}
.quote-mark.close{right:-40px;}

/* Footer */
.site-footer{position:absolute;left:0;top:2967px;width:1200px;height:136px;}
.footer-bar{border-top:10px solid var(--red);background:var(--black);height:58px;}
.footer-bar .container{width:1000px;display:flex;align-items:center;justify-content:space-between;height:48px;}
.footer-nav{display:flex;height:48px;}
.footer-nav a{font-family:var(--heading);font-size:12px;color:var(--white);display:flex;align-items:center;padding:0 18px;white-space:nowrap;}
.footer-nav a.active{background:var(--charcoal);border:1px solid #444;}
.social{display:flex;gap:6px;}
.social span{width:26px;height:26px;background:#555;border-radius:3px;display:block;}
.social span:first-child{background:var(--red);}
.footer-legal{background:#0e0e0e;height:78px;color:#999;font-size:12px;text-align:center;line-height:78px;}
</style>
</head>
<body>

<header class="site-header">
  <div class="container">
    <a class="brand" href="#">HARWICK AUDIT</a>
    <nav class="main-nav">
      <a class="active" href="#">HOME</a>
      <a href="#">OUR FIRM</a>
      <a href="#">ATTORNEYS</a>
      <a href="#">ISSUES &amp; CASES</a>
      <a href="#">CASE RESULT</a>
      <a href="#">CONTACT US</a>
    </nav>
  </div>
</header>

<section class="hero" role="img" aria-label="Photo of brass scales of justice in a wood-panelled courtroom">
  <div class="hero-copy">
    <h1 class="hero-title">LOREM IPSUM DOLOR SIT AMET</h1>
    <p class="hero-sub">LOREM IPSUM DOLOR SIT AMET</p>
    <div class="actions">
      <a class="btn-outline" href="#">LOREM IPSUM</a><a class="btn-outline" href="#">LOREM IPSUM</a>
    </div>
  </div>
</section>

<section class="firm">
  <h2 class="section-title">OUR FIRM</h2>
  <div class="firm-grid">
    <div class="firm-item">
      <div class="firm-icon">
        <svg width="54" height="54" viewBox="0 0 54 54" fill="#c8102e"><polygon points="27,4 4,16 50,16"/><rect x="4" y="18" width="46" height="4"/><rect x="8" y="24" width="6" height="18"/><rect x="19" y="24" width="6" height="18"/><rect x="30" y="24" width="6" height="18"/><rect x="41" y="24" width="6" height="18"/><rect x="3" y="44" width="48" height="5"/></svg>
      </div>
      <h3 class="item-title">LOREM IPSUM DOLOR CLAIMS</h3>
      <p class="item-text">Lorem ipsum dolor sit amet, consectetur adipiscing elit, sed do eiusmod tempor incididunt.</p>
      <a class="read-more" href="#">» READ MORE »</a>
    </div>
    <div class="firm-item">
      <div class="firm-icon">
        <svg width="58" height="50" viewBox="0 0 58 50" fill="#c8102e"><rect x="2" y="12" width="34" height="26" rx="2"/><path d="M36 18h10l9 10v10H36z"/><circle cx="13" cy="41" r="6"/><circle cx="46" cy="41" r="6"/><rect x="15" y="18" width="8" height="14" fill="#fff"/><rect x="12" y="21" width="14" height="8" fill="#fff"/></svg>
      </div>
      <h3 class="item-title">LOREM IPSUM DOLOR CLAIMS</h3>
      <p class="item-text">Lorem ipsum dolor sit amet, consectetur adipiscing elit, sed do eiusmod tempor incididunt.</p>
      <a class="read-more" href="#">» READ MORE »</a>
    </div>
    <div class="firm-item">
      <div class="firm-icon">
        <svg width="44" height="54" viewBox="0 0 44 54"><path d="M2 2h28l12 12v38H2z" fill="#c8102e"/><g fill="#fff"><rect x="9" y="20" width="26" height="3"/><rect x="9" y="28" width="26" height="3"/><rect x="9" y="36" width="26" height="3"/><rect x="9" y="12" width="14" height="3"/></g></svg>
      </div>
      <h3 class="item-title">LOREM IPSUM DOLOR CLAIMS</h3>
      <p class="item-text">Lorem ipsum dolor sit amet, consectetur adipiscing elit, sed do eiusmod tempor incididunt.</p>
      <a class="read-more" href="#">» READ MORE »</a>
    </div>
    <div class="firm-item">
      <div class="firm-icon">
        <svg width="52" height="52" viewBox="0 0 52 52"><path d="M34 4a12 12 0 0 0-11 16L4 39a5 5 0 0 0 9 9l19-19a12 12 0 0 0 16-11l-7 4-6-3-1-7 7-6z" fill="#c8102e"/></svg>
      </div>
      <h3 class="item-title">LOREM IPSUM DOLOR CLAIMS</h3>
      <p class="item-text">Lorem ipsum dolor sit amet, consectetur adipiscing elit, sed do eiusmod tempor incididunt.</p>
      <a class="read-more" href="#">» READ MORE »</a>
    </div>
  </div>
</section>

<section class="services">
  <h2 class="section-title">SERVICES</h2>
  <div class="service-grid">
    <div class="service-card">
      <div class="service-photo photo-law" role="img" aria-label="Photo of law books and documents on a desk"></div>
      <div class="service-label">LOREM IPSUM DOLOR</div>
      <p class="item-text">Lorem ipsum dolor sit amet, consectetur adipiscing elit, sed do eiusmod tempor incididunt.</p>
      <a class="read-more" href="#">» READ MORE »</a>
    </div>
    <div class="service-card">
      <div class="service-photo photo-gavel" role="img" aria-label="Photo of a wooden gavel resting on papers"></div>
      <div class="service-label">LOREM IPSUM DOLOR</div>
      <p class="item-text">Lorem ipsum dolor sit amet, consectetur adipiscing elit, sed do eiusmod tempor incididunt.</p>
      <a class="read-more" href="#">» READ MORE »</a>
    </div>
    <div class="service-card">
      <div class="service-photo photo-advisor" role="img" aria-label="Photo of a smiling client advisor"></div>
      <div class="service-label">LOREM IPSUM DOLOR</div>
      <p class="item-text">Lorem ipsum dolor sit amet, consectetur adipiscing elit, sed do eiusmod tempor incididunt.</p>
      <a class="read-more" href="#">» READ MORE »</a>
    </div>
  </div>
</section>

<section class="banner" role="img" aria-label="Photo of a judge's gavel on its block in dim light">
  <div class="banner-copy">
    <h2 class="banner-title">LOREM IPSUM DOLOR SIT AMET,<br>CONSECTETUR ADIPISCING ELIT</h2>
    <a class="btn-outline" href="#">LOREM IPSUM</a>
  </div>
</section>

<section class="about">
  <div class="about-photo" role="img" aria-label="Photo of a businesswoman in a grey suit with arms folded"></div>
  <div class="about-copy">
    <h2 class="about-title">LOREM IPSUM</h2>
    <p class="about-text">Sed ut perspiciatis unde omnis iste natus error sit voluptatem accusantium doloremque laudantium, totam rem aperiam, eaque ipsa quae ab illo inventore veritatis et quasi architecto beatae vitae dicta sunt explicabo. Nemo enim ipsam voluptatem quia voluptas sit aspernatur aut odit aut fugit, sed quia consequuntur magni dolores eos qui ratione voluptatem sequi nesciunt. Neque porro quisquam est, qui dolorem ipsum quia dolor sit amet, consectetur, adipisci velit, sed quia non numquam eius modi tempora incidunt ut labore et dolore magnam aliquam quaerat voluptatem.</p>
    <a class="btn-red" href="#">CLICK HERE</a>
  </div>
</section>

<section class="team">
  <h2 class="team-title">LOREM IPSUM</h2>
  <div class="team-grid">
    <div class="team-card">
      <div class="team-photo" role="img" aria-label="Portrait photo of a female team member"></div>
      <div class="team-label">LOREM IPSUM DOLOR</div>
    </div>
    <div class="team-card">
      <div class="team-photo" role="img" aria-label="Portrait photo of a male team member"></div>
      <div class="team-label">LOREM IPSUM DOLOR</div>
    </div>
    <div class="team-card">
      <div class="team-photo" role="img" aria-label="Portrait photo of a female team member"></div>
      <div class="team-label">LOREM IPSUM DOLOR</div>
    </div>
  </div>
</section>

<section class="testimonial">
  <h2 class="section-title">CLIENT TESTIMONIAL</h2>
  <div class="avatar" role="img" aria-label="Round portrait photo of the client"></div>
  <blockquote class="quote">
    <span class="quote-mark open">“</span>
    Lorem ipsum dolor sit amet, consectetur adipiscing elit. Aenean commodo ligula eget dolor. Aenean massa cum sociis natoque penatibus et magnis dis parturient montes, nascetur ridiculus mus. Donec quam felis, ultricies nec, pellentesque eu, pretium quis, sem.
    <span class="quote-mark close">”</span>
  </blockquote>
</section>

<footer class="site-footer">
  <div class="footer-bar">
    <div class="container">
      <nav class="footer-nav">
        <a class="active" href="#">HOME</a>
        <a href="#">OUR FIRM</a>
        <a href="#">ATTORNEYS</a>
        <a href="#">ISSUES &amp; CASES</a>
        <a href="#">CASE RESULT</a>
        <a href="#">CONTACT US</a>
      </nav>
      <div class="social" aria-label="Social links">
        <span></span><span></span><span></span><span></span>
      </div>
    </div>
  </div>
  <div class="footer-legal">Privacy | Copyright</div>
</footer>

</body>
</html>
```